Uni Camp Poster (Theme: Desert Oasis)

We require a poster design for our annual camp with the theme "desert oasis", please see the attached design brief for details.
We are the Meridian Fellowship (Mf), founded in 1996 at the Collingwood Institute of Learning. As one of the largest social clubs at the Collingwood Institute of Learning, Mf runs a variety of premier social and sporting events for University students.
Target Market(s)
18-19 year olds in Melbourne

```html
<!DOCTYPE html>
<html lang="en">
<head>
<meta charset="utf-8">
<title>Oasis: A Jorney Through the Sands – Camp Poster</title>
<link rel="stylesheet" href="https://fonts.googleapis.com/css2?family=Almendra:wght@700&family=Roboto+Condensed:wght@400;700&family=Oswald:wght@400;500&display=swap">
<style>
  :root {
    --sky-dark: #3e3428;
    --sky-mid: #7a5c3e;
    --sky-glow: #c99a62;
    --cloud: #8e8468;
    --pyramid: #4d7f7c;
    --palm-dark: #2c3420;
    --palm: #4a5330;
    --water: #3f3a2c;
    --dune-light: #e2c49a;
    --sand-light: #d6b586;
    --sand-deep: #a9825a;
    --band: rgba(70, 58, 46, 0.6);
    --white: #ffffff;
    --silver-hi: #ffffff;
    --silver-mid: #cfcfcf;
    --silver-lo: #6a6a6a;
  }
  * { margin: 0; padding: 0; box-sizing: border-box; }
  html, body { width: 1200px; height: 745px; overflow: hidden; background: #e3e3e3; }
  .poster {
    position: relative;
    width: 1200px;
    height: 745px;
    overflow: hidden;
    font-family: "Roboto Condensed", sans-serif;
    color: var(--white);
  }
  .scene {
    position: absolute; inset: 0;
    background:
      /* sand foreground */
      linear-gradient(180deg, transparent 86%, var(--sand-deep) 88%, var(--sand-light) 100%),
      /* palm band and water */
      radial-gradient(ellipse 40% 12% at 42% 84%, var(--water) 0%, rgba(63,58,44,0.8) 60%, transparent 100%),
      linear-gradient(180deg, transparent 60%, rgba(44,52,32,0.85) 66%, var(--palm) 74%, var(--palm-dark) 82%, transparent 88%),
      /* left palms */
      radial-gradient(ellipse 16% 40% at 6% 72%, var(--palm-dark) 0%, transparent 100%),
      /* right dunes */
      radial-gradient(ellipse 30% 22% at 90% 66%, var(--dune-light) 0%, rgba(226,196,154,0.4) 60%, transparent 100%),
      /* glass pyramid */
      radial-gradient(ellipse 20% 32% at 55% 38%, var(--pyramid) 0%, rgba(77,127,124,0.55) 55%, transparent 100%),
      /* right dark cliff */
      radial-gradient(ellipse 10% 30% at 100% 20%, #26302c 0%, transparent 100%),
      /* clouds */
      radial-gradient(ellipse 30% 18% at 18% 14%, var(--cloud) 0%, transparent 100%),
      radial-gradient(ellipse 50% 30% at 55% 58%, var(--sky-glow) 0%, transparent 80%),
      linear-gradient(180deg, var(--sky-dark) 0%, var(--sky-mid) 38%, var(--sky-glow) 62%, var(--sand-deep) 100%);
  }
  .presenter {
    position: absolute; top: 38px; left: 756px;
    width: 190px;
  }
  .presenter-name {
    display: flex; align-items: center; gap: 10px;
    font-family: "Oswald", sans-serif;
    font-weight: 500;
    font-size: 25px;
    line-height: 27px;
    letter-spacing: 0.3px;
    text-transform: uppercase;
  }
  .presenter-name .mark {
    flex: none;
    width: 38px; height: 38px; border-radius: 50%;
    border: 2px solid var(--white);
  }
  .presenter-tag {
    font-family: "Oswald", sans-serif;
    font-size: 11px; margin-top: 8px;
    text-align: center; padding-left: 40px;
  }
  .affiliation {
    position: absolute; top: 38px; left: 1040px; width: 100px;
    text-align: center;
    font-family: "Oswald", sans-serif;
    font-weight: 500;
    text-transform: uppercase;
  }
  .affiliation-name { font-size: 30px; line-height: 34px; }
  .affiliation-tag { font-size: 14px; line-height: 14px; margin-top: 8px; }
  .title {
    position: absolute; left: 0; right: 0;
    font-family: "Almendra", serif;
    font-weight: 700;
    font-size: 132px;
    line-height: 1;
    text-align: center;
    white-space: nowrap;
    background: linear-gradient(180deg, var(--silver-hi) 0%, var(--silver-mid) 35%, var(--silver-lo) 55%, var(--silver-hi) 80%, var(--silver-mid) 100%);
    -webkit-background-clip: text; background-clip: text;
    color: transparent;
    filter: drop-shadow(2px 3px 0 #1c1c1c) drop-shadow(0 4px 6px rgba(0,0,0,0.6));
  }
  .title-line-1 { top: 215px; padding-left: 10px; letter-spacing: 4px; }
  .title-line-2 { top: 350px; padding-left: 14px; }
  .date-band {
    position: absolute; top: 511px; left: 169px;
    width: 638px; height: 46px;
    background: var(--band);
  }
  .date {
    position: absolute; top: 511px; left: 0; right: 0; height: 46px;
    display: flex; align-items: center; justify-content: center;
    font-size: 32px; letter-spacing: 1px;
    text-shadow: 0 1px 3px rgba(0,0,0,0.5);
  }
  .date b { font-weight: 700; }
  .date sup { font-size: 16px; vertical-align: 13px; margin-right: 6px; }
  .date .small { font-size: 22px; margin-right: 8px; }
  .pricing {
    position: absolute; top: 571px; left: 0; width: 1150px;
    text-align: center;
    font-size: 24px; line-height: 28px; font-weight: 700; letter-spacing: 1px;
    text-shadow: 0 1px 3px rgba(0,0,0,0.6);
  }
  .pricing .small { font-size: 16px; font-weight: 400; }
  .pricing .divider { font-weight: 400; opacity: 0.7; margin: 0 14px; }
</style>
</head>
<body>
  <main class="poster">
    <div class="scene" role="img" aria-label="Desert oasis scene: a glass pyramid under cloudy amber sky, palm trees around a pool, a woman standing at the water's edge and two cats on the sand"></div>

    <div class="presenter">
      <div class="presenter-name"><span class="mark"></span><span>Meridian<br>Fellowship</span></div>
      <div class="presenter-tag">PRESENTS</div>
    </div>

    <div class="affiliation">
      <div class="affiliation-name">CSU</div>
      <div class="affiliation-tag">Affiliated<br>Club</div>
    </div>

    <h1 class="title title-line-1">Oasis: A Jorney</h1>
    <div class="title title-line-2">Through the Sands</div>

    <div class="date-band"></div>
    <div class="date">
      <b>11</b><sup>TH</sup><span class="small">TO</span><b>13</b><sup>TH</sup>MARCH 2022
    </div>

    <p class="pricing">
      $155 <span class="small">FOR</span> MEMBERS<span class="divider">|</span>$165 <span class="small">FOR</span> NON-MEMBERS
    </p>
  </main>
</body>
</html>
```